Engineering group involved with fire safety needs a business card

We need a business card design for a company based in Greece called "Varotis Group". We are engineers and specialized technicians, operating the following : a) Fire fighting equipment trade b) Installation , Inspection & Maintenance of fire extinguishers and fire protection systems c) Occupational Health & Safety (Risk assessment & management/ Staff training). We need a clear and simple card design. I uploaded a draft I made, in order to give you an idea of the company and how I currently imagine the design of the card. I also uploaded the logo in .png file format. We are always open to different, new suggestions and ideas you may want to submit.
Target Market(s)
industries, companies, managers, retail clients
Industry/Entity Type
Fire Safety
Contact Information for Business Card
Addresses & phone numbers (headquarters + branch), logo, name (you can find all the details on the uploaded files!)
Colors
Designer to choose colors to be used in the design.
Look and feel
Each slider illustrates characteristics of the customer's brand and the style your logo design should communicate.

```html
<!DOCTYPE html>
<html lang="en">
<head>
<meta charset="utf-8">
<title>Varotis Group – Business Card</title>
<link href="https://fonts.googleapis.com/css2?family=Lato:wght@400;700;900&display=swap" rel="stylesheet">
<style>
  :root {
    --backdrop: #2a2a2b;
    --card: #5f6467;
    --brand-red: #b51f24;
    --ink-light: #ffffff;
    --rule: #d9dadb;
  }
  * { box-sizing: border-box; margin: 0; padding: 0; }
  html, body { width: 1200px; height: 960px; overflow: hidden; }
  body {
    background: var(--backdrop);
    font-family: "Lato", Arial, sans-serif;
    color: var(--ink-light);
    position: relative;
  }
  .card {
    position: absolute;
    top: 192px;
    width: 328px;
    height: 574px;
    background: var(--card);
    border-radius: 12px;
    box-shadow: 0 6px 18px rgba(0,0,0,0.45);
    text-align: center;
  }
  .card--front { left: 248px; }
  .card--back { left: 680px; }

  .brand {
    position: absolute;
    left: 0; right: 0;
    top: 132px;
    display: flex;
    align-items: center;
    justify-content: center;
    gap: 10px;
  }
  .brand__square {
    width: 30px; height: 30px;
    background: var(--brand-red);
  }
  .brand__name {
    font-weight: 900;
    font-size: 27px;
    letter-spacing: 1px;
    color: var(--brand-red);
    text-transform: uppercase;
  }

  .holder {
    position: absolute; left: 0; right: 0; top: 255px;
  }
  .holder__name {
    font-weight: 900;
    font-size: 26px;
    color: var(--brand-red);
    text-transform: uppercase;
    line-height: 30px;
  }
  .holder__role {
    font-size: 14.5px;
    margin-top: 4px;
  }
  .rule {
    width: 170px; height: 1px;
    background: var(--rule);
    margin: 0 auto;
  }
  .rule--top { margin-top: 12px; }

  .contacts {
    margin-top: 18px;
    font-size: 15px;
    line-height: 19px;
  }
  .contacts .label { color: var(--brand-red); }
  .contacts .gap { margin-top: 6px; }
  .rule--bottom { margin-top: 16px; }

  .offices {
    margin-top: 14px;
    font-size: 15px;
    line-height: 19px;
  }
  .offices .label { color: var(--brand-red); }
  .offices .office + .office { margin-top: 10px; }

  .services {
    position: absolute; left: 0; right: 0; top: 246px;
    font-size: 15px;
  }
  .services .sep { margin: 0 6px; }
  .areas {
    position: absolute; left: 0; right: 0; top: 335px;
    list-style: none;
    font-weight: 700;
    font-size: 15.5px;
    line-height: 27.5px;
    text-transform: uppercase;
  }
  .website {
    position: absolute; left: 0; right: 0; top: 515px;
    font-size: 14px;
    letter-spacing: 3.2px;
  }
  .website .domain { color: var(--brand-red); }
</style>
</head>
<body>
  <section class="card card--front">
    <div class="brand">
      <span class="brand__square"></span>
      <span class="brand__name">Varotis Group</span>
    </div>

    <div class="holder">
      <h1 class="holder__name">Stavros Kallinos</h1>
      <p class="holder__role">Mechanical Engineer - OHS Consultant</p>
      <div class="rule rule--top"></div>

      <div class="contacts">
        <p><span class="label">Tel.</span> (HQ) +30 22910 45128</p>
        <p class="gap"><span class="label">Tel.</span> (BO) +30 210 6143972</p>
        <p><span class="label">Mob.</span> +30 694 215 80 31</p>
        <p>stavros.kallinos@varotisgroup.gr</p>
      </div>

      <div class="rule rule--bottom"></div>

      <div class="offices">
        <div class="office">
          <p class="label">Headquaters:</p>
          <p>12 Eleftherias Street, 19400 Koropi</p>
        </div>
        <div class="office">
          <p class="label">Branch Office:</p>
          <p>18 Agiou Nikolaou, 15231 Chalandri</p>
        </div>
      </div>
    </div>
  </section>

  <section class="card card--back">
    <div class="brand">
      <span class="brand__square"></span>
      <span class="brand__name">Varotis Group</span>
    </div>

    <p class="services">Installation<span class="sep">|</span>Inspection<span class="sep">|</span>Maintenance</p>

    <ul class="areas">
      <li>Fire Fighting Equipment</li>
      <li>Licensing &amp; Business Registration</li>
      <li>Occupatioanal Health &amp; Safety</li>
      <li>Staff Training</li>
    </ul>

    <p class="website">www.<span class="domain">varotisgroup</span>.gr</p>
  </section>
</body>
</html>
```